Website design for Australia Equine Insurance business

Website Design Brief
1. Introduction
This brief guides the development of a modern, interactive website for our next-generation equine insurance business. We aim to establish a strong digital presence with a website that embodies innovation, usability, and trust, leading to exceptional user experiences and high customer conversions.

2. Company Background
Our startup offers cutting-edge equine insurance solutions across Australia, leveraging emerging technologies for smarter risk assessment, customer engagement, and claims processing. Our commitment is to protect our customers' financial interests and their equine companions with unparalleled service and modern, flexible insurance options.

3. Objectives
The website should:

Highlight our innovative products, services, and unique value proposition.
Drive lead generation and customer conversion using engaging design elements and compelling CTAs.
Foster customer trust and loyalty through transparency, industry expertise, and interactive features.
Enable users to request quotes, purchase insurance, and file claims online in a seamless, intuitive manner.
Be responsive and user-friendly across all devices.

5. Design Requirements
Look and Feel
The design should reflect our brand's personality: innovative, modern, reliable, and committed to the equine community. It should use our brand colours and logo, ensuring a clean, fresh aesthetic. The style guide should promote consistency across fonts, buttons, form fields, etc.

User Interface
The website should display optimally across desktop, tablet, and mobile, with a focus on usability and accessibility. Clear navigation menus, intuitive search and filters, and easy access to important pages like "Get a Quote," "File a Claim," "Contact Us," etc., should be ensured.

Content
Content should be engaging, easily digestible, and serve to educate users about our unique services and the value of equine insurance. The site should also feature blog posts, video guides, and interactive FAQs to illustrate our industry expertise and the benefits of our next-gen approach.

Functionality
Smart Quote Calculator: An AI-driven quote calculator providing real-time estimates.
Digital Purchase and Claims: Facilitate insurance purchase and claims filing digitally, complemented by AI and blockchain tech for efficiency and transparency.
User Accounts: Customers should be able to manage their policies, payments, and claims through personalized accounts.
AI Chatbot: Implement a chatbot for automated customer support, query resolution, and guidance.
SEO and Analytics: Ensure the website is SEO-optimized and integrated with analytics tools like Searchly Analytics.
6. Timeline
We aim to complete the website design and development project within a 4-month timeframe, given the startup nature of our business. This includes stages of initial design, content creation, development, testing, and launch.

7. Budget
We understand the importance of investing in quality and are open to reasonable negotiations for ensuring the best output.

Target Market(s)

4. Target Audience Our target audience is tech-savvy horse owners, breeders, trainers, equestrian centres, and younger individuals interested in equine ownership, primarily aged between 18-45. They appreciate digital convenience, technological innovation, and quality service.

Industry/Entity Type

The equine insurance industry is a specialised branch of the broader insurance market, focusing on coverage for all things related to horses. It encompasses a wide range of coverage areas such as mortality insurance (life insurance for horses), medical coverage, loss of use, liability coverage, and more. The industry is one of passion and care, where the clientele often form a deeply emotional connection to their insured assets - their horses. It’s characterized by a strong focus on well-being, safety, and the financial protection of both the horses and their owners. This makes trust, professionalism, and expertise central to any successful equine insurance business. Our new venture is positioned as a next-generation equine insurance provider. This means we are blending traditional insurance offerings with cutting-edge technologies such as AI and machine learning for better risk assessment, seamless customer service, and efficient claims processing. The audience in this sector is diverse, ranging from individual horse owners and breeders to professional trainers and large equestrian centres. Many of our customers have a significant emotional and financial investment in their horses, so they need to feel reassured that their insurance provider understands and respects this. In designing for this industry, it's essential to strike a balance between sophistication and warmth, to reflect both our professional reliability and our understanding of the personal passion that drives our clients. The design needs to feel modern and innovative, signaling our next-gen approach, but also trustworthy and user-friendly, ensuring customers of all technological skill levels feel comfortable using our platform. Moreover, the design should convey a sense of our commitment to the equine community, showing that we're more than just a faceless corporation. We care deeply about the wellbeing of horses and their owners, and we're here to support them with quality insurance solutions tailored to their unique needs.

Coding

Coded - Design and coding required

Number of Pages Required

5+ page

Requirements
Must have
• Responsive Design: The website should be fully responsive, offering optimal viewing and interaction across a range of devices - desktop, tablet, and mobile. Intuitive Navigation: The site should feature an easy-to-understand navigation system that allows users to find the information they're seeking quickly and efficiently. Clear Branding: The design should consistently incorporate the company's logo, colors, and overall aesthetic, reinforcing brand recognition. Content: High-quality, relevant content that explains your services, highlights your unique selling propositions, and educates users about equine insurance. The language should be clear, concise, and engaging. Smart Quote Calculator: An interactive tool enabling potential customers to get real-time insurance quotes. Online Purchase and Claims Filing System: A streamlined, user-friendly process for customers to buy insurance and file claims online. Customer Accounts: A secure area for customers to manage their policies, track claims, and make payments. AI Chatbot: An automated chat feature providing immediate customer support and answering frequently asked questions. SEO Optimization: The site must be search engine friendly, with strategically placed keywords, meta tags, and an XML sitemap for better indexing by search engines. Analytics Integration: Integration with tools like Searchly Analytics for tracking and analyzing user behavior and site performance. Data Security: Implementation of strong security measures to protect user data, including SSL encryption. Accessibility: Compliance with Web Content Accessibility Guidelines (WCAG) to ensure the site is accessible to people with disabilities. Contact Information: Clearly visible and easily accessible contact details, including phone number, email, and physical address. Social Media Integration: Links to the company's social media profiles for enhanced customer engagement and brand visibility. Remember, while these are essential features, the goal should always be to provide a seamless, positive user experience that aligns with your brand's identity and goals.
Nice to have
• Interactive Features: Interactive elements like quizzes or calculators can engage users, offer value, and make your site more memorable. Video Content: Videos explaining your products, services, or the importance of equine insurance can be a dynamic way to share information and appeal to different learning styles. Live Chat: In addition to an AI chatbot, having a live chat option for immediate customer support could significantly enhance user experience and satisfaction. Personalisation: If your resources allow, personalised content based on user behaviour or preferences can make your website more engaging and relevant. Integrated Blog: A blog section featuring articles on equine health, insurance tips, case studies etc., could help establish your brand as a thought leader in the field and improve SEO. Multilingual Support: If your target audience includes non-English speakers, offering content in multiple languages could be a beneficial feature. Customer Testimonials/Reviews: Including testimonials or reviews from satisfied customers can build trust and offer social proof. Resource Library: A library of downloadable resources (guides, checklists, eBooks) could offer added value to your customers and potential leads. Interactive FAQ: A dynamic FAQ section, where users can find answers quickly, or even an FAQ chatbot, could enhance the user experience. Newsletter Signup: An easily accessible sign-up option for a regular newsletter to keep users informed about your services, industry news, and tips. Integration with Customer Relationship Management (CRM) Software: To manage leads and customer information effectively, if your business operations allow for this level of integration.
Should not have
• Cluttered Layout: Overcrowding pages with too much information, images, or other elements can make your website look messy and confusing, hindering usability. Irrelevant Content: Your website should focus on information that is relevant to your target audience and industry. Avoid including content that does not provide value or enhance understanding of your products or services. Complex Navigation: A website should not have a confusing navigation system. Users should be able to find what they're looking for quickly and easily. Inconsistent Design: Inconsistencies in fonts, colors, or overall design can make your website look unprofessional. The design should be consistent throughout all pages. Slow Loading Times: Large images, animations, or other elements that significantly slow down page loading times should be avoided. Slow websites can lead to a poor user experience and high bounce rates. Poor Mobile Experience: Given the prevalence of mobile browsing, a design that doesn't perform well on mobile devices is a definite no. Autoplay Media: Videos or audio clips that start playing automatically can be annoying to users and should generally be avoided. Inaccessible Content: Ensure that all content is accessible to users of all abilities. Avoid design elements that violate accessibility standards. Hidden Contact Information: Contact information should be easy to find. Do not hide it in obscure parts of the website. Pop-ups: While sometimes necessary for marketing strategies, excessive use of pop-ups can annoy users and distract from the main content. Outdated Plugins: Avoid using outdated plugins or technology that some users may not be able to load or that could pose security risks. Lack of Privacy Policy: A website must have a clear and accessible privacy policy. Not having one can damage trust and may also violate laws or regulations.

```html
<!DOCTYPE html>
<html lang="en">
<head>
<meta charset="utf-8">
<title>Canterra Equine Insurance</title>
<link href="https://fonts.googleapis.com/css2?family=Poppins:wght@400;500;600;700;800;900&display=swap" rel="stylesheet">
<style>
:root{
  --ink:#1f1d1e;
  --dark:#231f20;
  --text:#555;
  --muted:#888;
  --light:#f3f3f3;
  --field:#e9e9e9;
  --white:#fff;
  --gold:#f2b01e;
  --line:#d6d6d6;
}
*{margin:0;padding:0;box-sizing:border-box}
html,body{width:1200px;height:4963px;overflow:hidden}
body{position:relative;font-family:'Poppins',sans-serif;color:var(--ink);background:var(--white)}
.abs{position:absolute}
a{color:inherit;text-decoration:none}
.btn{position:absolute;display:flex;align-items:center;justify-content:center;border:2px solid var(--ink);font-size:12px;font-weight:700;text-transform:uppercase;letter-spacing:.2px;background:transparent;color:var(--ink)}
.section-title{position:absolute;left:0;width:1200px;text-align:center;font-size:33px;font-weight:800;text-transform:uppercase;letter-spacing:-.5px}
.section-title::after{content:"";display:block;width:56px;height:2px;background:#bbb;margin:10px auto 0}
.photo{position:absolute;overflow:hidden}

/* hero */
.hero{position:absolute;left:0;top:0;width:1200px;height:718px;background:linear-gradient(180deg,#5d6066 0%,#7c7f84 28%,#8d8a80 48%,#6d6a55 62%,#4f4b3a 78%,#3b3728 100%)}
.hero::after{content:"";position:absolute;inset:0;background:rgba(0,0,0,.18)}
.hero-horse{position:absolute;left:720px;top:70px;width:330px;height:600px;border-radius:45% 40% 20% 20%;background:radial-gradient(ellipse at 50% 40%,#e7dcc8 0%,#cdbfa6 55%,rgba(180,165,140,0) 75%)}
.nav{position:absolute;top:34px;left:81px;right:81px;height:40px;z-index:2;display:flex;align-items:center}
.brand{display:flex;align-items:center;gap:10px;color:var(--white);font-weight:600;font-size:30px;letter-spacing:3px;text-transform:uppercase}
.brand-dot{width:40px;height:40px;border-radius:50%;border:2px solid currentColor}
.menu{margin-left:auto;display:flex;align-items:center;gap:15px;list-style:none;color:var(--white);font-size:11.5px;font-weight:600;text-transform:uppercase}
.menu li{display:flex;align-items:center;gap:6px}
.user-btn{width:38px;height:38px;background:var(--white);display:flex;align-items:center;justify-content:center;margin-left:8px}
.hero-copy{position:absolute;left:88px;top:206px;z-index:2;color:var(--white)}
.hero-copy h1{font-size:86px;font-weight:900;line-height:.99;text-transform:uppercase;letter-spacing:-1px}
.hero-copy p{margin-top:16px;font-size:15px;font-weight:700;text-transform:uppercase}
.hero .btn{z-index:2;left:89px;top:534px;width:124px;height:42px;border-color:var(--white);color:var(--white);font-size:11px}
.call-box{position:absolute;left:763px;top:664px;width:348px;height:108px;background:var(--dark);z-index:3;display:flex;align-items:center;padding-left:42px;gap:18px;color:var(--white)}
.call-icon{width:54px;height:54px;border-radius:50%;background:var(--white);display:flex;align-items:center;justify-content:center}
.call-box small{display:block;font-size:14px;font-weight:500}
.call-box strong{display:block;font-size:27px;font-weight:700;line-height:1.2}

/* about */
.about-title{left:676px;top:940px;font-size:34px;font-weight:800;text-transform:uppercase;letter-spacing:-.5px}
.about-text{left:676px;top:1014px;width:410px;font-size:13.5px;line-height:22.2px;color:var(--text)}

/* services */
.services{position:absolute;left:0;top:1493px;width:1200px;height:688px;background:var(--light)}
.card{position:absolute;top:1656px;width:241px;height:370px;background:var(--white)}
.card .photo{left:0;top:0;width:241px;height:209px}
.card h3{position:absolute;left:30px;top:235px;font-size:12.5px;font-weight:700;text-transform:uppercase}
.card p{position:absolute;left:30px;top:262px;width:190px;font-size:12.5px;line-height:18.5px;color:var(--text)}
.card a{position:absolute;left:30px;top:331px;font-size:11.5px;font-weight:600;color:#999;text-decoration:underline;text-transform:uppercase}

/* quote */
.quote-title{left:160px;top:2356px;font-size:33px;font-weight:800;line-height:40px;text-transform:uppercase;letter-spacing:-.5px}
.quote-text{left:160px;top:2462px;width:430px;font-size:13.5px;line-height:22px;color:var(--text)}
.emblem{left:670px;top:2300px;width:360px;height:360px;border-radius:50%;background:radial-gradient(circle,#f4f4f4 0%,#e4e4e4 100%)}

/* blog */
.post{position:absolute;top:2880px;width:460px;height:342px}
.post .photo{inset:0}
.post .photo::after{content:"";position:absolute;inset:0;background:linear-gradient(180deg,rgba(0,0,0,0) 55%,rgba(0,0,0,.55) 100%)}
.post .date{position:absolute;left:42px;top:267px;color:#ddd;font-size:14px;font-weight:700;z-index:1}
.post h3{position:absolute;left:42px;top:286px;color:var(--white);font-size:22px;font-weight:800;text-transform:uppercase;z-index:1;white-space:nowrap}

/* testimonials */
.reviews{position:absolute;left:0;top:3432px;width:1200px;height:545px;background:var(--light)}
.review{position:absolute;top:3629px;height:204px;background:var(--white)}
.avatar{position:absolute;top:-34px;left:38px;width:72px;height:72px;border-radius:50%;background:radial-gradient(circle at 50% 40%,#b98d70 0%,#6b5446 60%,#3c3733 100%);border:3px solid var(--white)}
.quote-mark{position:absolute;top:14px;left:190px;font-size:90px;font-weight:800;color:#e4e4e4;line-height:1}
.review p{position:absolute;left:28px;top:62px;width:270px;font-size:12.2px;line-height:19.5px;color:var(--text)}
.review hr{position:absolute;left:28px;right:28px;top:144px;border:0;border-top:1px solid #e6e6e6}
.review h4{position:absolute;left:28px;top:158px;font-size:12.5px;font-weight:700;text-transform:uppercase}
.review small{position:absolute;left:28px;top:176px;font-size:10px;color:#aaa}
.stars{position:absolute;right:28px;top:160px;display:flex;gap:2px}
.dots{position:absolute;top:3884px;left:574px;display:flex;gap:10px}
.dots span{width:10px;height:10px;border-radius:50%;background:#c9c9c9}
.dots span.on{background:var(--ink)}

/* contact */
.contact-title{left:166px;top:4206px;font-size:35px;font-weight:800;line-height:40px;text-transform:uppercase;letter-spacing:-.5px}
.contact-title::after{content:"";display:block;width:56px;height:2px;background:#bbb;margin-top:10px}
.footer{position:absolute;left:0;top:4414px;width:1200px;height:549px;background:var(--dark);color:#cfcfcf}
.form-card{position:absolute;left:532px;top:4074px;width:451px;height:423px;background:var(--white);box-shadow:0 6px 30px rgba(0,0,0,.12);z-index:2}
.form-card label{position:absolute;font-size:10.5px;font-weight:700;text-transform:uppercase}
.field{position:absolute;height:40px;background:var(--field);font-size:11px;color:#8d8d8d;padding:0 14px;display:flex;align-items:center;justify-content:space-between}
.submit{position:absolute;left:26px;top:337px;width:400px;height:46px;background:var(--dark);color:var(--white);font-size:14px;font-weight:700;text-transform:uppercase;display:flex;align-items:center;justify-content:center}
.submit svg{position:absolute;right:20px}

.footer-brand{position:absolute;left:92px;top:244px;display:flex;align-items:center;gap:14px;color:var(--white);font-size:42px;font-weight:600;letter-spacing:5px;text-transform:uppercase}
.footer-brand .brand-dot{width:56px;height:56px}
.socials{position:absolute;left:148px;top:348px;display:flex;gap:10px}
.socials span{width:36px;height:36px;border-radius:50%;background:#3a3536}
.fcol{position:absolute;top:208px}
.fcol h5{color:var(--white);font-size:15.5px;font-weight:700;text-transform:uppercase;margin-bottom:14px}
.fcol li{list-style:none;font-size:11.5px;line-height:27px}
.info{display:flex;gap:10px;font-size:11.5px;line-height:16px;margin-bottom:20px}
.info svg{flex:none;margin-top:2px}
.fline{position:absolute;left:88px;right:88px;top:478px;border-top:1px solid #3d3839}
.copy{position:absolute;left:0;width:1200px;top:506px;text-align:center;font-size:11px;font-weight:600;color:var(--white);text-transform:uppercase}
.chat{position:absolute;left:1134px;top:458px;width:44px;height:44px;border-radius:50%;background:#5a5556;display:flex;align-items:center;justify-content:center}
</style>
</head>
<body>

<header class="hero">
  <div class="hero-horse" role="img" aria-label="Photo of a pale palomino horse standing by a wooden fence in a grassy field under a cloudy sky"></div>
  <nav class="nav">
    <a class="brand" href="#"><span class="brand-dot"></span>Canterra</a>
    <ul class="menu">
      <li><svg width="12" height="12" viewBox="0 0 12 12"><path d="M6 1 1 5.5h1.5V11h3V8h1v3h3V5.5H11z" fill="#fff"/></svg>Home</li>
      <li>About Us</li><li>Services/Products</li><li>Get a Quote</li><li>Contact Us</li><li>File a Claim</li><li>Blog</li>
      <li class="user-btn"><svg width="16" height="16" viewBox="0 0 16 16"><circle cx="8" cy="5" r="3.2" fill="#222"/><path d="M2 15c0-3.5 2.7-5.5 6-5.5s6 2 6 5.5z" fill="#222"/></svg></li>
    </ul>
  </nav>
  <div class="hero-copy">
    <h1>Canterra<br>Equine<br>Insurance</h1>
    <p>Generation equine insurance business</p>
  </div>
  <a class="btn" href="#">Get a Quote</a>
</header>
<div class="call-box">
  <span class="call-icon"><svg width="22" height="22" viewBox="0 0 24 24"><path d="M6.6 10.8a15.1 15.1 0 0 0 6.6 6.6l2.2-2.2a1 1 0 0 1 1-.25 11.4 11.4 0 0 0 3.6.57 1 1 0 0 1 1 1V20a1 1 0 0 1-1 1A17 17 0 0 1 3 4a1 1 0 0 1 1-1h3.5a1 1 0 0 1 1 1c0 1.25.2 2.45.57 3.57a1 1 0 0 1-.25 1z" fill="#222"/></svg></span>
  <div><small>Call Us Today:</small><strong>(0400) 555-218</strong></div>
</div>

<section aria-label="About">
  <div class="photo" style="left:189px;top:828px;width:276px;height:328px;background:linear-gradient(180deg,#a7b3c2 0%,#c7a26b 45%,#8b5a2b 70%,#7d8a3e 100%)" role="img" aria-label="Photo of a bay horse trotting through an autumn field"></div>
  <div class="photo" style="left:327px;top:973px;width:284px;height:343px;background:linear-gradient(160deg,#3f4a2c 0%,#8c8c7a 40%,#6e4c2e 70%,#c9b48e 100%);border:4px solid #fff" role="img" aria-label="Photo of a grey horse and a dark bay horse on a sunlit dirt track"></div>
  <div class="photo" style="left:100px;top:1158px;width:370px;height:230px;background:linear-gradient(180deg,#5f8a2f 0%,#78a23a 50%,#4d7a22 100%);border:4px solid #fff" role="img" aria-label="Photo of a chestnut foal galloping across green grass"></div>
  <h2 class="abs about-title">About Canterra</h2>
  <p class="abs about-text">Aenean sollicitudin, lorem quis bibendum auctor, nisi elit consequat ipsum, nec sagittis sem nibh id elit. Duis sed odio sit amet nibh vulputate cursus a sit amet mauris. Morbi accumsan ipsum velit. Nam nec tellus a odio tincidunt auctor a ornare odio. Sed non &nbsp;mauris vitae erat consequat auctor eu in elit. Class aptent taciti sociosqu ad litora torquent per conubia nostra, per inceptos himenaeos. Mauris in erat justo. Nullam ac urna eu felis dapibus condimentum sit...</p>
  <a class="btn" href="#" style="left:676px;top:1242px;width:120px;height:43px">Read More</a>
</section>

<section class="services" aria-label="Our services"></section>
<h2 class="section-title" style="top:1572px">Our Services</h2>
<article class="card" style="left:98px">
  <div class="photo" style="background:linear-gradient(180deg,#9fb4c7 0%,#c9c1a8 40%,#8a6a3a 70%,#6f8a3a 100%)" role="img" aria-label="Photo of a white mare with her chestnut foal in a paddock"></div>
  <h3>Mortality Insurance</h3><p>Protect your horses from unexpected loss or death with our comprehensive...</p><a href="#">Read More</a>
</article>
<article class="card" style="left:352px">
  <div class="photo" style="background:linear-gradient(180deg,#c8ccd2 0%,#8e6a4a 45%,#6f6a66 75%,#7a8a5a 100%)" role="img" aria-label="Photo of a bandaged horse being led from a horse trailer"></div>
  <h3>Medical Coverage</h3><p>Ensure your horses receive the best veterinary care with our insurance plans...</p><a href="#">Read More</a>
</article>
<article class="card" style="left:607px">
  <div class="photo" style="background:linear-gradient(120deg,#5a4030 0%,#8a6548 40%,#c8b7a2 70%,#9a8e80 100%)" role="img" aria-label="Photo of a man grooming a bay horse"></div>
  <h3>Liability Coverage</h3><p>Safeguard yourself against property damage or bodily injury claims caused...</p><a href="#">Read More</a>
</article>
<article class="card" style="left:861px">
  <div class="photo" style="background:linear-gradient(120deg,#2a2a2c 0%,#4a4a4e 40%,#d9d9d9 70%,#8a8a8a 100%)" role="img" aria-label="Photo of a man standing beside a black horse in a stable"></div>
  <h3>Customized Solutions</h3><p>Get personalized insurance plans tailored to your specific needs, providing...</p><a href="#">Read More</a>
</article>
<a class="btn" href="#" style="left:524px;top:2063px;width:152px;height:43px">Online Purhase</a>

<section aria-label="Get a quote">
  <h2 class="abs quote-title">Get a Horse Cover<br>Policy Quote Today</h2>
  <p class="abs quote-text">Aenean sollicitudin, lorem quis bibendum auctor, nisi elit consequat ipsum, nec sagittis sem nibh id elit. Duis sed odio sit amet nibh vulputate...</p>
  <a class="btn" href="#" style="left:160px;top:2552px;width:128px;height:44px">File a Claim</a>
  <div class="abs emblem" role="img" aria-label="Brand emblem area"></div>
</section>

<h2 class="section-title" style="top:2796px">Our Blog</h2>
<article class="post" style="left:-335px">
  <div class="photo" style="background:linear-gradient(180deg,#5c6a3a 0%,#7a6a45 60%,#4a3a28 100%)" role="img" aria-label="Photo of horses in a field"></div>
  <span class="date">05/30/23</span><h3>Some Heaing Here</h3>
</article>
<article class="post" style="left:135px">
  <div class="photo" style="background:linear-gradient(180deg,#2f3a24 0%,#3f4a2c 40%,#cfcfcf 60%,#5a3a24 85%,#3a2a1e 100%)" role="img" aria-label="Photo of a white horse prancing on a dirt path"></div>
  <span class="date">05/30/23</span><h3>Some Heaing Here</h3>
</article>
<article class="post" style="left:605px">
  <div class="photo" style="background:linear-gradient(180deg,#5a5a3a 0%,#c9a275 35%,#b58a5a 65%,#6f8a3a 100%)" role="img" aria-label="Photo of a palomino mare with her foal"></div>
  <span class="date">05/30/23</span><h3>Some Heaing Here</h3>
</article>
<article class="post" style="left:1073px">
  <div class="photo" style="background:linear-gradient(180deg,#4a4a3a 0%,#e0ddd5 45%,#7a6a4a 100%)" role="img" aria-label="Photo of a white horse in a meadow"></div>
  <span class="date">05/30/23</span><h3>Some Heaing Here</h3>
</article>
<a class="btn" href="#" style="left:524px;top:3278px;width:152px;height:43px">View All Blog</a>

<section class="reviews" aria-label="Testimonials"></section>
<h2 class="section-title" style="top:3506px">What Our Client Say</h2>
<article class="review" style="left:89px;width:329px">
  <div class="avatar" role="img" aria-label="Portrait of the client"></div><span class="quote-mark">&ldquo;</span>
  <p>I did a little experiment today: I took a blog that we did a few weeks ago, added MV3's advice, and asked Searchly to reindex...</p><hr>
  <h4>Marcus Whitfield</h4><small>Owner</small>
  <span class="stars"><svg width="70" height="12" viewBox="0 0 70 12"><g fill="#f2b01e"><path id="st" d="M6 0l1.8 3.9 4.2.4-3.2 2.8 1 4.1L6 9.1 2.2 11.2l1-4.1L0 4.3l4.2-.4z"/><use href="#st" x="14.5"/><use href="#st" x="29"/><use href="#st" x="43.5"/><use href="#st" x="58"/></g></svg></span>
</article>
<article class="review" style="left:437px;width:326px">
  <div class="avatar" role="img" aria-label="Portrait of the client"></div><span class="quote-mark">&ldquo;</span>
  <p>I did a little experiment today: I took a blog that we did a few weeks ago, added MV3's advice, and asked Searchly to reindex...</p><hr>
  <h4>Callum Brennan</h4><small>Owner</small>
  <span class="stars"><svg width="70" height="12" viewBox="0 0 70 12"><g fill="#f2b01e"><use href="#st"/><use href="#st" x="14.5"/><use href="#st" x="29"/><use href="#st" x="43.5"/><use href="#st" x="58"/></g></svg></span>
</article>
<article class="review" style="left:780px;width:330px">
  <div class="avatar" role="img" aria-label="Portrait of the client"></div><span class="quote-mark">&ldquo;</span>
  <p>I did a little experiment today: I took a blog that we did a few weeks ago, added MV3's advice, and asked Searchly to reindex...</p><hr>
  <h4>Dalia Okoro</h4><small>Owner</small>
  <span class="stars"><svg width="70" height="12" viewBox="0 0 70 12"><g fill="#f2b01e"><use href="#st"/><use href="#st" x="14.5"/><use href="#st" x="29"/><use href="#st" x="43.5"/><use href="#st" x="58"/></g></svg></span>
</article>
<div class="dots"><span></span><span class="on"></span><span></span></div>

<h2 class="abs contact-title">Get in Touch<br>With Us!</h2>

<footer class="footer">
  <div class="footer-brand"><span class="brand-dot"></span>Canterra</div>
  <div class="socials"><span role="img" aria-label="Social link"></span><span role="img" aria-label="Social link"></span><span role="img" aria-label="Social link"></span><span role="img" aria-label="Social link"></span></div>
  <div class="fcol" style="left:437px"><h5>Quick Links</h5><ul><li>HOMEAbout Us</li><li>Services/Products</li><li>Get a Quote</li><li>Contact Us</li><li>File a claim</li><li>Blog</li></ul></div>
  <div class="fcol" style="left:651px"><h5>Our Services</h5><ul><li>Mortality Insurance</li><li>Medical Coverage</li><li>Liability Coverage</li><li>Customized Solutions</li></ul></div>
  <div class="fcol" style="left:917px;width:210px"><h5>Contact Info</h5>
    <div class="info"><svg width="13" height="10" viewBox="0 0 13 10"><rect x=".5" y=".5" width="12" height="9" fill="none" stroke="#fff"/><path d="M.5.5l6 5 6-5" fill="none" stroke="#fff"/></svg><span>Email:<br>hello@canterra-equine.com.au</span></div>
    <div class="info"><svg width="13" height="13" viewBox="0 0 24 24"><path d="M6.6 10.8a15.1 15.1 0 0 0 6.6 6.6l2.2-2.2a1 1 0 0 1 1-.25 11.4 11.4 0 0 0 3.6.57 1 1 0 0 1 1 1V20a1 1 0 0 1-1 1A17 17 0 0 1 3 4a1 1 0 0 1 1-1h3.5a1 1 0 0 1 1 1c0 1.25.2 2.45.57 3.57a1 1 0 0 1-.25 1z" fill="#fff"/></svg><span>Phone:<br>+61 400 555 218</span></div>
    <div class="info"><svg width="11" height="14" viewBox="0 0 11 14"><path d="M5.5 0A5.5 5.5 0 0 0 0 5.5C0 9.6 5.5 14 5.5 14S11 9.6 11 5.5A5.5 5.5 0 0 0 5.5 0zm0 7.7a2.2 2.2 0 1 1 0-4.4 2.2 2.2 0 0 1 0 4.4z" fill="#fff"/></svg><span>Location:<br>Some address line goes here city name country</span></div>
  </div>
  <div class="fline"></div>
  <p class="copy">&copy; Copyright 2023 Canterra Equine Insurance all rights reserved</p>
  <div class="chat"><svg width="22" height="20" viewBox="0 0 22 20"><path d="M11 1C5.5 1 1 4.6 1 9c0 2.3 1.2 4.3 3.1 5.8L3 19l4.6-2.5c1 .3 2.2.5 3.4.5 5.5 0 10-3.6 10-8S16.5 1 11 1z" fill="#fff"/><circle cx="7" cy="9" r="1.3" fill="#5a5556"/><circle cx="11" cy="9" r="1.3" fill="#5a5556"/><circle cx="15" cy="9" r="1.3" fill="#5a5556"/></svg></div>
</footer>

<form class="form-card" aria-label="Contact form">
  <label style="left:26px;top:36px">Name*</label>
  <div class="field" style="left:26px;top:58px;width:197px">Enter your name</div>
  <label style="left:231px;top:36px">Date*</label>
  <div class="field" style="left:231px;top:58px;width:195px">Enter your email</div>
  <label style="left:26px;top:106px">Phone*</label>
  <div class="field" style="left:26px;top:126px;width:197px">Enter phone number</div>
  <label style="left:231px;top:106px">Date*</label>
  <div class="field" style="left:231px;top:126px;width:195px">Select date<svg width="9" height="6" viewBox="0 0 9 6"><path d="M1 1l3.5 3.5L8 1" fill="none" stroke="#333" stroke-width="1.5"/></svg></div>
  <label style="left:26px;top:180px">Messages*</label>
  <div class="field" style="left:26px;top:200px;width:400px;height:112px;align-items:flex-start;padding-top:14px">Type your text...</div>
  <div class="submit">Submit Now<svg width="18" height="18" viewBox="0 0 24 24"><path d="M22 2 2 10l7 3 3 7 10-18zM9 13l13-11" fill="none" stroke="#fff" stroke-width="2" stroke-linejoin="round"/></svg></div>
</form>

</body>
</html>
```